Business Card and Letterhead Design Project

I am starting my own building design business in Melbourne. The business will use my experience to help people make balanced life choices for building and renovating. My target audience is women -particularly mothers. I aim to be approachable and economical. I would like to see a design that uses greens or blues - natural colours. A lot of my work balances design and construction management so design should be flexible.

I want a double sided business card design and a letterhead design that I can use on all office correspondance

Design should have a clean crisp feel - a bit edgey in a feminine way.

Target Market(s)

Potential clients.

Industry/Entity Type

Construction

Requirements
Must have
• Brackenridge Design Studio
Harriet Oakley B.Arch

0497 283 541
harriet@brackenridgedesignstudio.example.au

14 Pembury Road
Ashgrove Heights VIC 3190
brackenridgedesignstudio.example.au
Nice to have
• Should have a calming feel to make me seem approachable but still professional.
Should not have
• No photos on the card or building plans.

```html
<!DOCTYPE html>
<html lang="en">
<head>
<meta charset="utf-8">
<title>Brackenridge Design Studio – Business Card</title>
<link rel="stylesheet" href="https://fonts.googleapis.com/css2?family=Roboto+Condensed:wght@300;400;700&display=swap">
<style>
  :root {
    --stage: #e9eae7;
    --card-white: #ffffff;
    --brand-green: #7ab648;
    --brand-blue: #1f8fd6;
    --ink-grey: #6d6e70;
    --shadow: rgba(0, 0, 0, 0.14);
  }
  * { margin: 0; padding: 0; box-sizing: border-box; }
  html, body {
    width: 1200px;
    height: 872px;
    overflow: hidden;
    background: var(--stage);
    font-family: "Roboto Condensed", "Arial Narrow", sans-serif;
  }
  .stage {
    position: relative;
    width: 1200px;
    height: 872px;
  }
  .card {
    position: absolute;
    top: 288px;
    width: 520px;
    height: 297px;
    box-shadow: 0 6px 18px var(--shadow);
    overflow: hidden;
  }
  .card--front { left: 60px; background: var(--card-white); }
  .card--back  { left: 620px; background: var(--brand-green); }

  /* Front: contact block */
  .person { position: absolute; left: 36px; top: 30px; }
  .person__name {
    color: var(--brand-green);
    font-size: 20px;
    font-weight: 400;
    letter-spacing: 0.3px;
    text-transform: uppercase;
  }
  .person__title {
    color: var(--ink-grey);
    font-size: 9px;
    letter-spacing: 0.6px;
    margin-top: 2px;
  }
  .contact {
    position: absolute;
    left: 36px;
    top: 88px;
    color: var(--ink-grey);
    font-size: 10px;
    line-height: 13px;
    text-transform: uppercase;
    letter-spacing: 0.2px;
    list-style: none;
  }
  .contact__gap { margin-top: 8px; }

  /* Wordmark */
  .wordmark {
    position: absolute;
    text-transform: uppercase;
    text-align: left;
  }
  .wordmark__name {
    font-size: 25px;
    font-weight: 700;
    letter-spacing: 0.5px;
    line-height: 1;
  }
  .wordmark__sub {
    font-size: 12px;
    font-weight: 300;
    letter-spacing: 1px;
    margin-top: 3px;
  }
  .wordmark--front { right: 28px; top: 186px; }
  .wordmark--front .wordmark__name { color: var(--brand-blue); }
  .wordmark--front .wordmark__sub  { color: var(--brand-green); }

  /* Front: colour bands */
  .bands { position: absolute; left: 0; bottom: 40px; width: 520px; height: 12px; }
  .bands__initials {
    position: absolute;
    left: 336px;
    bottom: 39px;
    line-height: 14px;
    color: var(--ink-grey);
    font-size: 10px;
    letter-spacing: 0.5px;
  }

  /* Back */
  .wordmark--reverse {
    color: var(--card-white);
    left: 50%;
    top: 50%;
    transform: translate(-45%, -55%);
  }
  .wordmark--reverse .wordmark__name { font-size: 27px; }
  .wordmark--reverse .wordmark__sub  { font-size: 13px; letter-spacing: 1.2px; }
</style>
</head>
<body>
<main class="stage">
  <section class="card card--front" aria-label="Business card front">
    <div class="person">
      <h1 class="person__name">Harriet Oakley</h1>
      <p class="person__title">B.ARCH</p>
    </div>
    <ul class="contact">
      <li>T: 0497 283 541</li>
      <li class="contact__gap">E: harriet@brackenridgedesignstudio.example.au</li>
      <li class="contact__gap">A: 14 Pembury Road</li>
      <li>Ashgrove Heights VIC 3190</li>
      <li>brackenridgedesignstudio.example.au</li>
    </ul>
    <div class="wordmark wordmark--front">
      <p class="wordmark__name">Brackenridge</p>
      <p class="wordmark__sub">Design Studio</p>
    </div>
    <svg class="bands" viewBox="0 0 520 12" aria-hidden="true">
      <rect x="0" y="0" width="328" height="12" fill="var(--brand-green)"/>
      <rect x="368" y="0" width="152" height="12" fill="var(--brand-blue)"/>
    </svg>
    <span class="bands__initials">BDS</span>
  </section>

  <section class="card card--back" aria-label="Business card back">
    <div class="wordmark wordmark--reverse">
      <p class="wordmark__name">Brackenridge</p>
      <p class="wordmark__sub">Design Studio</p>
    </div>
  </section>
</main>
</body>
</html>
```